Design business card using existing logo.

PLEASE DO NOT USE "RED WHITE & BLACK" color combo! Thank you.

Try different color combos such as:
- Vintage colors like brown, orange, gold, blue (not all together but a combo of 1 or 3
- Blue, w/ grey, or silver or white, Blue monochromatic can work as well.
- Use monochromatic variations on back (just an idea)

- Include full name, "Quillmark Records" on at least one side.

Target Market(s)

Teens

Industry/Entity Type

Business

Colors
3277b5
ffc214
f04a50
f78f20

```html
<!DOCTYPE html>
<html lang="en">
<head>
<meta charset="utf-8">
<title>Quillmark Records – Business Card</title>
<link rel="stylesheet" href="https://fonts.googleapis.com/css2?family=Arimo:wght@400;500&display=swap">
<style>
  :root {
    --backdrop: #e4e4e4;
    --card-light: #f4f4f4;
    --card-dark: #3a3a3a;
    --accent-grey: #c9c9c9;
    --ink: #111111;
    --paper: #ffffff;
  }
  * { margin: 0; padding: 0; box-sizing: border-box; }
  html, body {
    width: 1200px;
    height: 1000px;
    overflow: hidden;
    background: var(--backdrop);
    font-family: "Arimo", Arial, sans-serif;
  }
  .card {
    position: absolute;
    left: 267px;
    width: 669px;
    height: 401px;
    overflow: hidden;
  }
  .card svg { display: block; width: 100%; height: 100%; }
  .card--front { top: 85px; background: var(--card-light); }
  .card--back { top: 527px; background: var(--card-dark); }

  .holder-name { font-size: 28px; fill: var(--ink); letter-spacing: 0.3px; }
  .holder-title { font-size: 13px; fill: var(--ink); letter-spacing: 0.2px; }
  .logo-frame { fill: none; stroke: var(--ink); stroke-width: 1.5; }
  .logo-label { font-size: 15px; fill: var(--ink); }
  .contact-box { fill: var(--card-dark); }
  .contact-text { font-size: 13.6px; fill: var(--paper); }
  .contact-text--large { font-size: 14.5px; }
  .contact-icon { fill: var(--paper); }
  .contact-icon-line { fill: none; stroke: var(--paper); stroke-width: 1.6; }
  .envelope-fold { fill: none; stroke: var(--card-dark); }
  .edge-tab--dark { fill: var(--card-dark); }
  .edge-tab--light { fill: var(--accent-grey); }
  .brand-frame { fill: none; stroke: var(--paper); stroke-width: 2; }
  .brand-name { font-size: 40px; fill: var(--paper); letter-spacing: 0.5px; }
</style>
</head>
<body>

<section class="card card--front" aria-label="Business card front">
  <svg viewBox="0 0 669 401" xmlns="http://www.w3.org/2000/svg">
    <polygon class="edge-tab--dark" points="0,62 25,85 25,320 0,343"/>

    <text class="holder-name" x="185" y="82" text-anchor="middle">MARCUS HALE</text>
    <text class="holder-title" x="182" y="101" text-anchor="middle">MANAGING DIRECTOR</text>

    <polygon class="logo-frame" points="181,125 266,173 266,273 181,321 96,273 96,173"/>
    <text class="logo-label" x="181" y="219" text-anchor="middle">COMPANY</text>
    <text class="logo-label" x="181" y="238" text-anchor="middle">LOGO</text>

    <!-- address -->
    <rect class="contact-box" x="347" y="60" width="61" height="52"/>
    <rect class="contact-box" x="421" y="60" width="248" height="52"/>
    <path class="contact-icon" d="M377.5,73 a9,9 0 0 1 9,9 c0,6 -9,16 -9,16 c0,0 -9,-10 -9,-16 a9,9 0 0 1 9,-9 z M377.5,78.5 a3.5,3.5 0 1 0 0.01,0 z" fill-rule="evenodd"/>
    <text class="contact-text" x="436" y="81">YOUR CITY ADDRESS</text>
    <text class="contact-text" x="436" y="99">STREET LOCATION, NY CITY,USA</text>

    <!-- phone -->
    <rect class="contact-box" x="347" y="136" width="61" height="52"/>
    <rect class="contact-box" x="421" y="136" width="248" height="52"/>
    <path class="contact-icon" d="M371,148 l5,-1 l3,7 l-3,3 c1,4 4,8 8,10 l3,-3 l7,3 l-1,5 c-2,2 -5,2 -8,1 c-7,-3 -13,-10 -15,-17 c-1,-3 -1,-6 1,-8 z"/>
    <text class="contact-text" x="436" y="158">+1 555 0142 8836</text>
    <text class="contact-text" x="436" y="174">+1 555 0178 2041</text>

    <!-- web -->
    <rect class="contact-box" x="347" y="213" width="61" height="52"/>
    <rect class="contact-box" x="421" y="213" width="248" height="52"/>
    <g class="contact-icon-line">
      <circle cx="377.5" cy="239" r="10"/>
      <ellipse cx="377.5" cy="239" rx="4.5" ry="10"/>
      <line x1="367.5" y1="239" x2="387.5" y2="239"/>
      <line x1="369.5" y1="233" x2="385.5" y2="233"/>
      <line x1="369.5" y1="245" x2="385.5" y2="245"/>
    </g>
    <text class="contact-text" x="436" y="243">WWW.QUILLMARK.COM</text>

    <!-- email -->
    <rect class="contact-box" x="347" y="289" width="61" height="52"/>
    <rect class="contact-box" x="421" y="289" width="248" height="52"/>
    <rect class="contact-icon" x="363" y="305" width="30" height="20"/>
    <polyline class="envelope-fold" points="363,305 378,317 393,305" stroke-width="1.6"/>
    <path class="envelope-fold" d="M363,325 L374,314 M382,314 L393,325" stroke-width="1.2"/>
    <text class="contact-text contact-text--large" x="436" y="320">info@quillmark.com</text>
  </svg>
</section>

<section class="card card--back" aria-label="Business card back">
  <svg viewBox="0 0 669 401" xmlns="http://www.w3.org/2000/svg">
    <polygon class="edge-tab--light" points="0,60 28,85 28,318 0,343"/>
    <polygon class="edge-tab--light" points="669,60 641,85 641,318 669,343"/>
    <rect class="brand-frame" x="55" y="162" width="561" height="76"/>
    <text class="brand-name" x="335.5" y="214" text-anchor="middle">QUILLMARK RECORDS</text>
  </svg>
</section>

</body>
</html>
```